Business card required for IT Consultancy Business - Tealbrook Consulting.
Company provides the whole nine yards of services across IT Architecture, design and execution.
Basically we provide consulting services to help businesses make sure their technology is enabling their business strategy.
Design for front and back required.
We would like the front of the card to inlcude:
Name
Title
Mobile number
email address
www.tbkc.com.au
Company logos attached.
Thank you
Industry/Entity Type
Business
Contact Information for Business Card
Name
Title
Mobile number
email address
www.tbkc.com.au
Look and feel
Each slider illustrates characteristics of the customer's brand and the style your logo design should communicate.

```html
<!DOCTYPE html>
<html lang="en">
<head>
<meta charset="utf-8">
<title>Tealbrook Consulting – Business Card</title>
<link rel="stylesheet" href="https://fonts.googleapis.com/css2?family=Arimo:wght@400;700&display=swap">
<style>
  :root {
    --backdrop: #d9d9db;
    --card-white: #ffffff;
    --brand-orange: #ee5a2c;
    --brand-orange-light: #f26d3c;
    --brand-blue: #1f7bc1;
    --ink: #1e1e1e;
  }
  * { box-sizing: border-box; margin: 0; padding: 0; }
  html, body {
    width: 1200px; height: 1000px; overflow: hidden;
    background: var(--backdrop);
    font-family: "Arimo", Arial, sans-serif;
  }
  .canvas { position: relative; width: 1200px; height: 1000px; }

  .card {
    position: absolute;
    width: 540px; height: 308px;
    border-radius: 30px;
    overflow: hidden;
    box-shadow: 0 10px 24px rgba(0,0,0,0.18);
  }

  /* Front */
  .card--front { left: 70px; top: 150px; background: var(--card-white); }
  .front-band { position: absolute; left: 0; bottom: 0; width: 100%; height: 150px; }
  .front-brand {
    position: absolute; left: 40px; top: 52px;
    display: flex; align-items: center; gap: 12px;
  }
  .brand-dot {
    width: 34px; height: 34px; border-radius: 50%;
    background: var(--brand-orange);
  }
  .brand-name {
    font-weight: 700; font-size: 30px; color: var(--brand-blue);
    letter-spacing: 0.5px;
  }
  .holder { position: absolute; left: 88px; top: 120px; }
  .holder-name {
    font-weight: 700; font-size: 19px; letter-spacing: 1px;
    text-transform: uppercase;
  }
  .holder-name .first { color: var(--brand-orange); }
  .holder-name .last { color: var(--brand-blue); }
  .holder-title { font-size: 18px; color: var(--ink); margin-top: 2px; }
  .contacts { list-style: none; margin-top: 16px; }
  .contacts li {
    display: flex; align-items: center; gap: 8px;
    font-size: 15px; color: var(--ink); margin-bottom: 5px;
  }
  .contact-icon { width: 18px; height: 18px; flex: none; }

  /* Back */
  .card--back {
    left: 590px; top: 560px;
    background: linear-gradient(135deg, var(--brand-orange-light), var(--brand-orange));
    color: var(--card-white);
  }
  .back-brand {
    position: absolute; left: 0; right: 0; top: 100px;
    display: flex; justify-content: center; align-items: center; gap: 14px;
  }
  .back-brand .brand-dot { background: var(--card-white); width: 40px; height: 40px; }
  .back-brand .brand-name { color: var(--card-white); font-size: 36px; }
  .back-web {
    position: absolute; left: 0; right: 0; bottom: 36px;
    text-align: center; font-size: 18px; letter-spacing: 1px;
  }
</style>
</head>
<body>
<main class="canvas">

  <section class="card card--front" aria-label="Business card front">
    <svg class="front-band" viewBox="0 0 540 150" preserveAspectRatio="none" aria-hidden="true">
      <path d="M0 150 L0 128 Q260 70 540 0 L540 150 Z" fill="var(--brand-orange)"/>
      <path d="M0 128 Q260 70 540 0 L540 14 Q260 84 0 142 Z" fill="var(--card-white)"/>
    </svg>

    <div class="front-brand">
      <span class="brand-dot"></span>
      <span class="brand-name">Tealbrook Consulting</span>
    </div>

    <div class="holder">
      <p class="holder-name"><span class="first">Marlo</span> <span class="last">Ventress</span></p>
      <p class="holder-title">CEO</p>
      <ul class="contacts">
        <li>
          <svg class="contact-icon" viewBox="0 0 18 18" aria-hidden="true">
            <circle cx="9" cy="9" r="8" fill="var(--brand-orange)" stroke="var(--brand-blue)" stroke-width="1.5"/>
            <rect x="6" y="4.5" width="6" height="9" rx="1" fill="none" stroke="#fff" stroke-width="1.3"/>
          </svg>
          014-2857-306
        </li>
        <li>
          <svg class="contact-icon" viewBox="0 0 18 18" aria-hidden="true">
            <circle cx="9" cy="9" r="8" fill="var(--brand-orange)" stroke="var(--brand-blue)" stroke-width="1.5"/>
            <rect x="4.5" y="6" width="9" height="6" fill="none" stroke="#fff" stroke-width="1.2"/>
            <path d="M4.5 6 L9 9.5 L13.5 6" fill="none" stroke="#fff" stroke-width="1.2"/>
          </svg>
          hello@tbkc.com.au
        </li>
        <li>
          <svg class="contact-icon" viewBox="0 0 18 18" aria-hidden="true">
            <circle cx="9" cy="9" r="8" fill="var(--brand-orange)" stroke="var(--brand-blue)" stroke-width="1.5"/>
            <circle cx="9" cy="9" r="4.5" fill="none" stroke="#fff" stroke-width="1.2"/>
            <path d="M4.5 9 H13.5 M9 4.5 Q6.5 9 9 13.5 Q11.5 9 9 4.5" fill="none" stroke="#fff" stroke-width="1"/>
          </svg>
          www.tbkc.com.au
        </li>
      </ul>
    </div>
  </section>

  <section class="card card--back" aria-label="Business card back">
    <div class="back-brand">
      <span class="brand-dot"></span>
      <span class="brand-name">Tealbrook Consulting</span>
    </div>
    <p class="back-web">www.tbkc.com.au</p>
  </section>

</main>
</body>
</html>
```